KL Taxidermy

I need business Cards with my logo and a background photo of one of my taxidermy mounts.
I would like a black back drop behind it all and what ever looks best for my contact information (red or white?)
Garrick Pembley
592-718-4409
kltaxidermy482@mailnook.example
Chatterloom page

```html
<!DOCTYPE html>
<html lang="en">
<head>
<meta charset="utf-8">
<title>KL Taxidermy – Business Cards</title>
<link href="https://fonts.googleapis.com/css2?family=Oswald:wght@500;600&family=Lato:wght@400&display=swap" rel="stylesheet">
<style>
  :root {
    --backdrop: #2a2522;
    --card-black: #0d0d0d;
    --ink-white: #f2f2f2;
    --ink-soft: #d6d6d6;
    --divider: #3a3a3a;
    --photo-dark: #1f242b;
    --photo-mid: #3a4048;
    --photo-light: #7d8086;
  }
  * { box-sizing: border-box; margin: 0; padding: 0; }
  html, body { width: 1200px; height: 844px; overflow: hidden; }
  body {
    background: var(--backdrop);
    display: flex;
    align-items: center;
    justify-content: center;
    gap: 40px;
  }
  .card {
    width: 550px;
    height: 314px;
    border-radius: 4px;
    overflow: hidden;
    position: relative;
    box-shadow: 0 10px 30px rgba(0,0,0,.45);
  }
  .card-front {
    background: var(--card-black);
    display: flex;
    align-items: center;
  }
  .brand {
    width: 270px;
    display: flex;
    align-items: center;
    justify-content: center;
    gap: 10px;
  }
  .brand-mark {
    width: 18px;
    height: 18px;
    background: var(--ink-white);
  }
  .brand-name {
    font-family: "Oswald", sans-serif;
    font-weight: 600;
    font-size: 28px;
    letter-spacing: 2px;
    color: var(--ink-white);
    text-transform: uppercase;
  }
  .divider {
    width: 1px;
    height: 150px;
    background: var(--divider);
  }
  .contact {
    padding-left: 28px;
    color: var(--ink-soft);
    font-family: "Lato", sans-serif;
    font-size: 13.5px;
  }
  .contact-name {
    font-family: "Oswald", sans-serif;
    font-weight: 500;
    font-size: 19px;
    color: var(--ink-white);
    text-transform: uppercase;
    margin-bottom: 10px;
  }
  .contact-line {
    display: flex;
    align-items: center;
    gap: 8px;
    line-height: 22px;
  }
  .contact-line.social { margin-top: 10px; }
  .contact-icon { width: 12px; height: 12px; flex: none; }
  .social-dot {
    width: 13px; height: 13px; border-radius: 50%;
    background: var(--ink-white); flex: none;
  }
  .card-back {
    background: radial-gradient(ellipse at 60% 55%, var(--photo-light) 0%, var(--photo-mid) 35%, var(--photo-dark) 80%);
  }
</style>
</head>
<body>
  <section class="card card-front">
    <div class="brand">
      <span class="brand-mark"></span>
      <span class="brand-name">KL Taxidermy</span>
    </div>
    <div class="divider"></div>
    <div class="contact">
      <p class="contact-name">Garrick Pembley</p>
      <p class="contact-line">
        <svg class="contact-icon" viewBox="0 0 12 12"><path d="M2 1h2.5l1 2.5-1.4 1a6 6 0 0 0 3.4 3.4l1-1.4 2.5 1V11A9.5 9.5 0 0 1 1 2z" fill="#f2f2f2"/></svg>
        592-718-4409
      </p>
      <p class="contact-line">
        <svg class="contact-icon" viewBox="0 0 12 12"><rect x="0.5" y="2" width="11" height="8" fill="#f2f2f2"/><path d="M0.5 2l5.5 4.5L11.5 2" fill="none" stroke="#0d0d0d" stroke-width="1"/></svg>
        kltaxidermy482@mailnook.example
      </p>
      <p class="contact-line social">
        <span class="social-dot"></span>
        chatterloom@kltaxidermy
      </p>
    </div>
  </section>
  <section class="card card-back" role="img" aria-label="Photograph of a white ram taxidermy mount with curled horns, resting on a rock against a dark backdrop"></section>
</body>
</html>
```